Firma sucht ansprechendes Einfahrtsschild
Zielgruppe
Firmen, sowie Privatpersonen / Laufkundschaft
Aufgabenstellung
Wir suchen für unser Hof ein neues Einfahrtsschild wie z.B. unser selbstversuch Hofschild 3.6.2015 // es hat auch jemand man etwas für uns gemacht vor langer zeit was aber nie benutzt wurde siehe M1 ///
wir suchen mehr etwas was den Leuten auffällt und das wesentliche rüber bringt.

```html
<!DOCTYPE html>
<html lang="de">
<head>
<meta charset="utf-8">
<title>Einfahrtsschild Wäscherei Brandel</title>
<link href="https://fonts.googleapis.com/css2?family=Montserrat:wght@500;600;700;800&family=Advent+Pro:wght@400&display=swap" rel="stylesheet">
<style>
  :root {
    --purple: #483e85;
    --green: #78ad41;
    --white: #ffffff;
    --ink: #1a1a1a;
    --backdrop: #2a2a2a;
  }
  html, body {
    margin: 0;
    padding: 0;
    width: 1200px;
    height: 1200px;
    overflow: hidden;
    background: var(--backdrop);
  }
  .sign {
    position: absolute;
    left: 48px;
    top: 180px;
    width: 1104px;
    height: 780px;
    background: var(--white);
    font-family: "Montserrat", sans-serif;
  }
  .top-band {
    position: absolute;
    left: 0;
    top: 19px;
    width: 1104px;
    height: 160px;
  }
  .top-band svg { display: block; width: 100%; height: 100%; }
  .top-band__title {
    position: absolute;
    right: 52px;
    top: 0;
    height: 160px;
    line-height: 160px;
    margin: 0;
    color: var(--white);
    font-weight: 800;
    font-size: 114px;
    letter-spacing: 1px;
  }
  .brand-mark {
    position: absolute;
    left: 60px;
    top: 295px;
    width: 236px;
    height: 236px;
    border-radius: 50%;
    background: var(--purple);
  }
  .brand-name {
    position: absolute;
    right: 58px;
    top: 250px;
    margin: 0;
    text-align: right;
    color: var(--purple);
    font-weight: 700;
    white-space: nowrap;
  }
  .brand-name__prefix {
    display: block;
    font-size: 46px;
    line-height: 50px;
  }
  .brand-name__main {
    display: block;
    font-size: 150px;
    line-height: 150px;
    letter-spacing: -2px;
  }
  .tagline {
    position: absolute;
    right: 58px;
    top: 470px;
    margin: 0;
    font-family: "Advent Pro", sans-serif;
    font-size: 34px;
    letter-spacing: 3px;
    color: var(--ink);
    white-space: nowrap;
  }
  .audience {
    position: absolute;
    right: 58px;
    top: 530px;
    margin: 0;
    font-weight: 600;
    font-size: 44px;
    letter-spacing: 3px;
    color: var(--green);
    white-space: nowrap;
  }
  .bottom-band {
    position: absolute;
    left: 0;
    top: 622px;
    width: 1104px;
    height: 139px;
    background: var(--purple);
    color: var(--white);
    text-align: center;
    line-height: 139px;
    font-weight: 500;
    font-size: 88px;
    letter-spacing: 4px;
    margin: 0;
  }
</style>
</head>
<body>
  <div class="sign">
    <div class="top-band">
      <svg viewBox="0 0 1776 258" preserveAspectRatio="none" aria-hidden="true">
        <rect x="0" y="0" width="1776" height="258" fill="var(--green)"/>
        <polygon points="0,0 270,0 58,129 270,258 0,258" fill="var(--purple)"/>
        <polygon points="267,0 327,0 115,129 327,258 267,258 58,129" fill="var(--white)"/>
        <polygon points="387,0 447,0 235,129 447,258 387,258 175,129" fill="var(--white)"/>
        <polygon points="507,0 567,0 355,129 567,258 507,258 295,129" fill="var(--white)"/>
      </svg>
      <h1 class="top-band__title">WÄSCHEREI</h1>
    </div>

    <div class="brand-mark"></div>
    <h2 class="brand-name">
      <span class="brand-name__prefix">Wäscherei</span>
      <span class="brand-name__main">Brandel</span>
    </h2>
    <p class="tagline">Sauberkeit und Frische aus dem Meisterbetrieb</p>
    <p class="audience">FÜR GEWERBE UND PRIVAT</p>

    <p class="bottom-band">PARKPLÄTZE IM HOF</p>
  </div>
</body>
</html>
```